Postcard Design

We are a full service lawn maintenace and landscapig company. Everything from maintenance, fertilizer programs, to design and install.
I would like the card to have a classy look including our logo which is attached. The logo would just have to contain the lettering and the swooshes not the pine tree background if not needed.

Industry/Entity Type

It Company

```html
<!DOCTYPE html>
<html lang="en">
<head>
<meta charset="utf-8">
<title>Tall Cedar Landscaping – Postcard</title>
<link rel="stylesheet" href="https://fonts.googleapis.com/css2?family=Source+Sans+3:wght@400;600;700&display=swap">
<style>
  :root {
    --lawn-deep: #2f7a1c;
    --lawn-mid: #4f9e2c;
    --lawn-light: #6cb83e;
    --straw-deep: #6e5232;
    --straw-mid: #9c7c52;
    --straw-light: #c2a477;
    --ink-white: #ffffff;
    --ink-shadow: rgba(0, 0, 0, 0.55);
  }
  * { margin: 0; padding: 0; box-sizing: border-box; }
  html, body {
    width: 1200px;
    height: 863px;
    overflow: hidden;
    background: #ffffff;
  }
  .postcard {
    position: relative;
    width: 1200px;
    height: 863px;
    overflow: hidden;
    font-family: "Source Sans 3", "Myriad Pro", Arial, sans-serif;
    color: var(--ink-white);
  }
  .backdrop {
    position: absolute;
    inset: 0;
    display: block;
  }
  .headline {
    position: absolute;
    left: 0;
    top: 50px;
    width: 1200px;
    font-weight: 700;
    font-size: 99px;
    line-height: 100px;
    letter-spacing: 0;
    white-space: nowrap;
    text-shadow: 2px 3px 6px var(--ink-shadow), 0 0 2px rgba(0,0,0,0.4);
  }
  .headline span { display: block; }
  .headline .line-one { padding-left: 104px; }
  .headline .line-two { padding-left: 238px; }
  .services {
    position: absolute;
    left: 313px;
    top: 334px;
    width: 880px;
    font-weight: 700;
    font-size: 39px;
    line-height: 51px;
    letter-spacing: 0.2px;
    white-space: nowrap;
    text-shadow: 2px 2px 4px var(--ink-shadow), 0 0 2px rgba(0,0,0,0.5);
  }
  .services span { display: block; }
  .contact {
    position: absolute;
    left: 92px;
    top: 636px;
    white-space: nowrap;
    text-shadow: 1px 2px 4px rgba(0,0,0,0.35);
  }
  .contact-lead {
    font-weight: 400;
    font-size: 40px;
    line-height: 44px;
  }
  .contact-phone {
    font-weight: 700;
    font-size: 75px;
    line-height: 80px;
    letter-spacing: 0.5px;
  }
  .contact-email {
    font-weight: 400;
    font-size: 40px;
    line-height: 44px;
  }
  .contact-email strong { font-weight: 700; }
  .brand {
    position: absolute;
    left: 640px;
    top: 668px;
    width: 530px;
    display: flex;
    align-items: center;
    gap: 18px;
  }
  .brand-dot {
    flex: none;
    width: 34px;
    height: 34px;
    border-radius: 50%;
    background: var(--ink-white);
  }
  .brand-name {
    font-weight: 700;
    font-size: 54px;
    line-height: 52px;
    letter-spacing: 2px;
    text-transform: uppercase;
    white-space: nowrap;
    color: var(--ink-white);
  }
</style>
</head>
<body>
  <main class="postcard">
    <svg class="backdrop" width="1200" height="863" viewBox="0 0 1200 863" role="img"
         aria-label="Photograph split down the middle: lush green lawn with a person's white shoes on the left, dry brown patchy grass on the right">
      <defs>
        <linearGradient id="lawn-green" x1="0" y1="0" x2="0" y2="1">
          <stop offset="0" stop-color="var(--lawn-light)"/>
          <stop offset="0.5" stop-color="var(--lawn-mid)"/>
          <stop offset="1" stop-color="var(--lawn-deep)"/>
        </linearGradient>
        <linearGradient id="lawn-dry" x1="0" y1="0" x2="1" y2="1">
          <stop offset="0" stop-color="var(--straw-mid)"/>
          <stop offset="0.5" stop-color="var(--straw-light)"/>
          <stop offset="1" stop-color="var(--straw-deep)"/>
        </linearGradient>
        <linearGradient id="lawn-seam" x1="0" y1="0" x2="1" y2="0">
          <stop offset="0" stop-color="var(--lawn-mid)" stop-opacity="1"/>
          <stop offset="1" stop-color="var(--lawn-mid)" stop-opacity="0"/>
        </linearGradient>
      </defs>
      <rect x="0" y="0" width="1200" height="863" fill="url(#lawn-dry)"/>
      <rect x="0" y="0" width="600" height="863" fill="url(#lawn-green)"/>
      <rect x="590" y="0" width="30" height="863" fill="url(#lawn-seam)"/>
    </svg>

    <h1 class="headline">
      <span class="line-one">Get the lawn you’ve</span>
      <span class="line-two">always dreamed of.</span>
    </h1>

    <p class="services">
      <span>We are a full service lawn maintenace and</span>
      <span>landscapeing company. We handle everything</span>
      <span>from maintenance, fertilizer programs, to</span>
      <span>design and installing.</span>
    </p>

    <div class="contact">
      <p class="contact-lead">For more information call</p>
      <p class="contact-phone">05 5512 3487</p>
      <p class="contact-email">or email: <strong>info@tcedar.com</strong></p>
    </div>

    <div class="brand">
      <span class="brand-dot"></span>
      <p class="brand-name">Tall Cedar<br>Landscaping</p>
    </div>
  </main>
</body>
</html>
```